Verpackungsdesign für Parfüm gesucht
Zielgruppe
Wir werden eine Marke unter dem Namen ORAMU mit Parfüm auf dem Markt bringen und benötigen hierfür ein hochwertiges Design . Unsre Zielgruppe ist m/w/d und zwischen 16 und 60 Jahre.
Aufgabenstellung
Bei der Verpackung handelt es sich um eine Schiebeschachtel. Wir benötigen das Design nur für die Außenhülle, nicht für den Schuber.
Pflichtangaben auf der Verpackung sind unser Logo, Eau de Parfum, NOIR ELEVATE, 20 ml e 0.67 FL OZ,
Natural Spray Vaporisateur,

```html
<!DOCTYPE html>
<html lang="de">
<head>
<meta charset="utf-8">
<title>ORAMU – Außenhülle Schiebeschachtel</title>
<link rel="stylesheet" href="https://fonts.googleapis.com/css2?family=Open+Sans:wght@300;400&display=swap">
<style>
  :root {
    --paper: #ffffff;
    --box-black: #000000;
    --fold-line: #1c1c1c;
    --frame-silver: #b9b9b9;
    --text-silver: #d2d2d2;
    --logo-silver: #d8d8d8;
  }
  html, body {
    margin: 0;
    padding: 0;
    width: 1200px;
    height: 698px;
    overflow: hidden;
    background: var(--paper);
  }
  .dieline {
    display: block;
    width: 1200px;
    height: 698px;
  }
  .dieline text {
    font-family: "Open Sans", Arial, sans-serif;
    fill: var(--text-silver);
  }
  .flap, .sleeve { fill: var(--box-black); }
  .fold { stroke: var(--fold-line); stroke-width: 1; }
  .panel-frame {
    fill: none;
    stroke: var(--frame-silver);
    stroke-width: 2;
  }
  .rule { stroke: var(--frame-silver); stroke-width: 1; }
  .spine-url { font-size: 16px; font-weight: 300; letter-spacing: 1px; }
  .brand-name {
    font-weight: 300;
    fill: var(--logo-silver) !important;
  }
  .brand-name--front { font-size: 50px; letter-spacing: 7px; }
  .brand-name--back { font-size: 44px; letter-spacing: 5px; }
  .product-type { font-size: 16px; font-weight: 300; letter-spacing: 1px; }
  .product-name { font-size: 26px; font-weight: 300; letter-spacing: 2.5px; }
  .product-detail { font-size: 11px; font-weight: 400; }
  .origin, .address { font-size: 11px; font-weight: 400; }
</style>
</head>
<body>
<svg class="dieline" viewBox="0 0 1160 675" preserveAspectRatio="xMidYMid meet" xmlns="http://www.w3.org/2000/svg">
  <polygon class="flap" points="55,88 173,62 173,612 55,585"/>

  <rect class="sleeve" x="173" y="62" width="915" height="550"/>
  <line class="fold" x1="266" y1="62" x2="266" y2="612"/>
  <line class="fold" x1="633" y1="62" x2="633" y2="612"/>
  <line class="fold" x1="726" y1="62" x2="726" y2="612"/>

  <text class="spine-url" transform="translate(226 336) rotate(-90)" text-anchor="middle">WWW.ORAMU.DE</text>

  <g class="front-panel">
    <rect class="panel-frame" x="285" y="79" width="331" height="517" rx="12"/>
    <text class="brand-name brand-name--front" x="450" y="183" text-anchor="middle">ORAMU</text>
    <text class="product-type" x="449" y="488" text-anchor="middle">EAU DE PARFUM</text>
    <text class="product-name" x="450" y="521" text-anchor="middle">NOIR ELEVATE</text>
    <line class="rule" x1="343" y1="534" x2="557" y2="534"/>
    <text class="product-detail" x="343" y="553">NATURAL SPRAY  VAPORISATEUR</text>
    <line class="rule" x1="513" y1="541" x2="513" y2="556"/>
    <text class="product-detail" x="518" y="553">℮ 20 ml</text>
  </g>

  <text class="spine-url" transform="translate(686 336) rotate(-90)" text-anchor="middle">WWW.ORAMU.DE</text>

  <g class="back-panel">
    <rect class="panel-frame" x="741" y="79" width="331" height="517" rx="12"/>
    <text class="origin" x="910" y="382" text-anchor="middle">MADE IN GERMANY</text>
    <text class="brand-name brand-name--back" x="910" y="444" text-anchor="middle">ORAMU</text>
    <line class="rule" x1="835" y1="461" x2="985" y2="461"/>
    <text class="address" x="910" y="487" text-anchor="middle">DUFTWEG 12</text>
    <text class="address" x="910" y="504" text-anchor="middle">D-40210 MUSTERSTADT</text>
    <text class="address" x="910" y="521" text-anchor="middle">WWW.ORAMU.DE</text>
  </g>
</svg>
</body>
</html>
```